Vornel Technologies business card design

We need a business card designed with our new logo. it would be great if the card could communicate it is a technology based company.

Target Market(s)

system integrators

Industry/Entity Type

technology, IOT

Contact Information for Business Card

Name, designation, Address, telephone number, email address

Requirements
Must have
• logo and company name
Nice to have
• something to do with technology

```html
<!DOCTYPE html>
<html lang="en">
<head>
<meta charset="utf-8">
<title>Vornel Technologies – Business Card</title>
<link rel="stylesheet" href="https://fonts.googleapis.com/css2?family=Roboto:wght@400;500;700&display=swap">
<style>
  :root {
    --backdrop: #6a5843;
    --card-light: #ffffff;
    --card-dark: #4a4a4b;
    --ink: #4a4a4a;
    --ink-soft: #6e6e6e;
    --accent: #f7941d;
    --rule: #c9c9c9;
    --logo-light: #e6e6e6;
  }
  * { margin: 0; padding: 0; box-sizing: border-box; }
  html, body { width: 900px; height: 1200px; overflow: hidden; }
  body {
    background: var(--backdrop);
    font-family: "Roboto", Arial, sans-serif;
    position: relative;
  }
  .card {
    position: absolute;
    left: 84px;
    width: 732px;
    height: 435px;
    border-radius: 30px;
    overflow: hidden;
    box-shadow: 0 6px 18px rgba(0,0,0,0.35);
  }
  .card--front { top: 135px; background: var(--card-light); }
  .card--back { top: 705px; background: var(--card-dark); }

  .brand {
    position: absolute;
    display: flex;
    align-items: center;
    gap: 18px;
  }
  .brand__mark { width: 46px; height: 46px; flex: none; }
  .brand__name {
    font-weight: 500;
    font-size: 40px;
    letter-spacing: 1px;
    line-height: 1;
    text-transform: uppercase;
  }
  .card--front .brand { left: 150px; top: 60px; }
  .card--front .brand__mark { background: var(--accent); }
  .card--front .brand__name { color: var(--ink); }
  .card--back .brand { left: 50%; top: 50%; transform: translate(-50%, -50%); }
  .card--back .brand__mark { background: var(--logo-light); }
  .card--back .brand__name { color: var(--logo-light); font-size: 44px; }

  .contact { position: absolute; left: 270px; top: 210px; color: var(--ink); }
  .contact__name { color: var(--accent); font-weight: 700; font-size: 30px; line-height: 1.1; }
  .contact__role { font-size: 21px; color: var(--ink-soft); margin-top: 4px; }
  .contact__rule { width: 70px; height: 2px; background: var(--rule); margin: 14px 0 16px; }
  .contact__address { font-size: 20px; line-height: 26px; }
  .contact__lines { list-style: none; margin-top: 12px; font-size: 19px; line-height: 26px; }
  .contact__lines li { display: flex; align-items: center; gap: 10px; }
  .contact__icon { width: 15px; height: 15px; fill: var(--accent); flex: none; }

  .card__band-accent {
    position: absolute; left: 0; bottom: 0; width: 270px; height: 14px; background: var(--accent);
  }
  .card__band-line {
    position: absolute; left: 270px; right: 0; bottom: 0; height: 4px; background: var(--rule);
  }
</style>
</head>
<body>
  <section class="card card--front">
    <div class="brand">
      <span class="brand__mark"></span>
      <span class="brand__name">Vornel Technologies</span>
    </div>

    <div class="contact">
      <p class="contact__name">Reed Matthews</p>
      <p class="contact__role">Managing Director</p>
      <div class="contact__rule"></div>
      <p class="contact__address">48 Harrow Lane, Suite B<br>Leeds, UK LS2 7QT</p>
      <ul class="contact__lines">
        <li>
          <svg class="contact__icon" viewBox="0 0 24 24" aria-hidden="true"><path d="M6.6 10.8a15.1 15.1 0 0 0 6.6 6.6l2.2-2.2a1 1 0 0 1 1-.25 11.4 11.4 0 0 0 3.6.57 1 1 0 0 1 1 1V20a1 1 0 0 1-1 1A17 17 0 0 1 3 4a1 1 0 0 1 1-1h3.5a1 1 0 0 1 1 1c0 1.25.2 2.45.57 3.57a1 1 0 0 1-.25 1z"/></svg>
          +00 000 000 0000
        </li>
        <li>
          <svg class="contact__icon" viewBox="0 0 24 24" aria-hidden="true"><path d="M2 5h20v14H2z M2 5l10 8 10-8" fill="var(--accent)"/><path d="M3 6l9 7 9-7" fill="none" stroke="#fff" stroke-width="2"/></svg>
          r_matthews@vorneltechnologies.co.uk
        </li>
      </ul>
    </div>

    <div class="card__band-accent"></div>
    <div class="card__band-line"></div>
  </section>

  <section class="card card--back">
    <div class="brand">
      <span class="brand__mark"></span>
      <span class="brand__name">Vornel Technologies</span>
    </div>
  </section>
</body>
</html>
```